Need a new logo/business card for a cafe

I need a new logo and business card for a café. The café is called "Ladle", and we have a reputation for making a high quality cup of espresso coffee. I would like the business card design to reflect this "high quality". Our baristas craft our customers coffee with care to achieve this result. I would like to see designs that include a warm latte brown color. The card will be single sided to allow the rear to be used as a loyalty card which means the design will need to include space for our business address, phone number, and facebook page details. The uploaded logo is already in use on the café front window, and if it can be incorporated or used that would be great, but I am open to completely new designs as well. Thank you.
Updates
Thank you to all for the submissions. There's quite a few I like now, the hardest part will be choosing! I've set up a poll for added feedback from my own contacts and will wait on results from that.
Hello, more great designs coming in, thank you very much. There's quite a few that I really like, so my biggest challenge is going to be choosing one. Thanks again for your time, and I'll get onto the hard task of making that choice. Marisa
Industry/Entity Type
Cafe
Look and feel
Each slider illustrates characteristics of the customer's brand and the style your logo design should communicate.

```html
<!DOCTYPE html>
<html lang="en">
<head>
<meta charset="utf-8">
<title>Ladle – Business Card Concepts</title>
<link rel="stylesheet" href="https://fonts.googleapis.com/css2?family=Open+Sans:wght@400;600&family=Orbitron:wght@600&family=Kaushan+Script&display=swap">
<style>
  :root{
    --stage-light:#e4e4e4;
    --stage-dark:#3a3a3a;
    --cream:#fbf7f3;
    --cream-warm:#f6e2d3;
    --peach:#edcfb7;
    --latte-light:#ddc9bd;
    --latte:#a88f82;
    --latte-dark:#8d7467;
    --espresso:#4a2c1e;
    --ink:#3a2a22;
    --white:#ffffff;
  }
  *{margin:0;padding:0;box-sizing:border-box}
  html,body{width:1200px;height:582px;overflow:hidden}
  body{
    background:radial-gradient(ellipse 70% 95% at 30% 70%, var(--stage-light) 0%, #a9a9a9 50%, var(--stage-dark) 100%);
    position:relative;
    font-family:"Open Sans",Arial,sans-serif;
  }
  .card{position:absolute;width:552px;height:304px}
  .card--classic{left:41px;top:82px}
  .card--tech{left:605px;top:193px}
  .card__shape{position:absolute;inset:0;width:552px;height:304px}
  .contact{position:absolute;left:31px;top:44px;list-style:none}
  .contact__item{display:flex;align-items:center;height:35px;gap:6px;color:var(--ink);font-size:14.5px;letter-spacing:.5px}
  .card--tech .contact{left:27px;top:38px}
  .card--tech .contact__item{font-family:"Orbitron","Open Sans",sans-serif;font-weight:600;font-size:14px;letter-spacing:1.6px;color:var(--espresso)}
  .icon{width:18px;height:20px;flex:none}
  .social-square{width:17px;height:17px;background:#3b5998;border-radius:2px;flex:none;margin-right:2px}
  .address{position:absolute;left:128px;top:237px;display:flex;gap:6px;color:var(--ink);font-size:12.5px;line-height:15px;letter-spacing:.4px}
  .address .icon{width:10px;height:14px;margin-top:1px}
  .address__lines{list-style:none}
  .brand{position:absolute;left:395px;top:195px;width:140px;text-align:center;
    font-family:"Kaushan Script","Open Sans",cursive;font-size:36px;color:var(--espresso);line-height:1}
</style>
</head>
<body>

<!-- Concept A -->
<section class="card card--classic" aria-label="Ladle business card, classic type">
  <svg class="card__shape" viewBox="0 0 552 304" aria-hidden="true">
    <defs>
      <clipPath id="a-card"><path d="M12,2 H462 Q550,2 550,90 V290 Q550,302 538,302 H115 Q2,302 2,195 V14 Q2,2 12,2 Z"/></clipPath>
      <clipPath id="a-lower"><path d="M0,190 C120,238 260,222 365,160 S500,100 552,110 V304 H0 Z"/></clipPath>
      <linearGradient id="a-top" x1="0" x2="1"><stop offset="0" stop-color="var(--cream-warm)"/><stop offset="1" stop-color="var(--cream)"/></linearGradient>
      <linearGradient id="a-bottom" x1="0" x2="1"><stop offset="0" stop-color="var(--latte-light)"/><stop offset=".55" stop-color="var(--latte)"/><stop offset="1" stop-color="var(--latte-dark)"/></linearGradient>
    </defs>
    <g clip-path="url(#a-card)">
      <rect width="552" height="304" fill="url(#a-bottom)"/>
      <path d="M0,198 C120,246 260,230 365,168 S500,108 552,118" fill="none" stroke="var(--latte-dark)" stroke-width="10"/>
      <path d="M0,190 C120,238 260,222 365,160 S500,100 552,110 V0 H0 Z" fill="url(#a-top)" stroke="var(--white)" stroke-width="14"/>
      <path d="M0,186 C120,234 260,218 365,156 S500,96 552,106" fill="none" stroke="var(--peach)" stroke-width="5"/>
    </g>
    <path d="M12,2 H462 Q550,2 550,90 V290 Q550,302 538,302 H115 Q2,302 2,195 V14 Q2,2 12,2 Z" fill="none" stroke="var(--peach)" stroke-width="5"/>
    <path clip-path="url(#a-lower)" d="M12,2 H462 Q550,2 550,90 V290 Q550,302 538,302 H115 Q2,302 2,195 V14 Q2,2 12,2 Z" fill="none" stroke="var(--latte-dark)" stroke-width="5"/>
  </svg>
  <ul class="contact">
    <li class="contact__item"><svg class="icon" viewBox="0 0 20 20"><circle cx="10" cy="10" r="8.5" fill="none" stroke="var(--ink)" stroke-width="1.5"/><path d="M7,5 l2,2.5 -1.3,1.3 q1,2.3 3.5,3.5 l1.3,-1.3 2.5,2 -1.6,1.8 q-4.5,-0.6 -7.8,-6.7Z" fill="var(--ink)"/></svg>123.456.7890</li>
    <li class="contact__item"><svg class="icon" viewBox="0 0 20 24"><rect x="5" y="3" width="10" height="20" rx="2" fill="none" stroke="var(--ink)" stroke-width="1.5"/><line x1="8" y1="20" x2="12" y2="20" stroke="var(--ink)"/></svg>123.456.7890</li>
    <li class="contact__item"><span class="social-square"></span>ourpage.com/</li>
  </ul>
  <div class="address">
    <svg class="icon" viewBox="0 0 10 14"><path d="M5,0 a4.5,4.5 0 0 1 4.5,4.5 c0,3 -4.5,9.5 -4.5,9.5 s-4.5,-6.5 -4.5,-9.5 A4.5,4.5 0 0 1 5,0Z" fill="var(--ink)"/><circle cx="5" cy="4.5" r="1.7" fill="var(--latte-light)"/></svg>
    <ul class="address__lines"><li>Address line 1</li><li>Address line 2</li><li>Address line 3</li></ul>
  </div>
  <div class="brand">Ladle</div>
</section>

<!-- Concept B -->
<section class="card card--tech" aria-label="Ladle business card, technical type">
  <svg class="card__shape" viewBox="0 0 552 304" aria-hidden="true">
    <defs>
      <clipPath id="b-card"><path d="M12,2 H462 Q550,2 550,90 V290 Q550,302 538,302 H115 Q2,302 2,195 V14 Q2,2 12,2 Z"/></clipPath>
      <clipPath id="b-lower"><path d="M0,190 C120,238 260,222 365,160 S500,100 552,110 V304 H0 Z"/></clipPath>
      <linearGradient id="b-top" x1="0" x2="1"><stop offset="0" stop-color="var(--cream-warm)"/><stop offset="1" stop-color="var(--cream)"/></linearGradient>
      <linearGradient id="b-bottom" x1="0" x2="1"><stop offset="0" stop-color="var(--latte-light)"/><stop offset=".55" stop-color="var(--latte)"/><stop offset="1" stop-color="var(--latte-dark)"/></linearGradient>
    </defs>
    <g clip-path="url(#b-card)">
      <rect width="552" height="304" fill="url(#b-bottom)"/>
      <path d="M0,198 C120,246 260,230 365,168 S500,108 552,118" fill="none" stroke="var(--latte-dark)" stroke-width="10"/>
      <path d="M0,190 C120,238 260,222 365,160 S500,100 552,110 V0 H0 Z" fill="url(#b-top)" stroke="var(--white)" stroke-width="14"/>
      <path d="M0,186 C120,234 260,218 365,156 S500,96 552,106" fill="none" stroke="var(--peach)" stroke-width="5"/>
    </g>
    <path d="M12,2 H462 Q550,2 550,90 V290 Q550,302 538,302 H115 Q2,302 2,195 V14 Q2,2 12,2 Z" fill="none" stroke="var(--peach)" stroke-width="5"/>
    <path clip-path="url(#b-lower)" d="M12,2 H462 Q550,2 550,90 V290 Q550,302 538,302 H115 Q2,302 2,195 V14 Q2,2 12,2 Z" fill="none" stroke="var(--latte-dark)" stroke-width="5"/>
  </svg>
  <ul class="contact">
    <li class="contact__item"><svg class="icon" viewBox="0 0 20 20"><circle cx="10" cy="10" r="8.5" fill="none" stroke="var(--ink)" stroke-width="1.5"/><path d="M7,5 l2,2.5 -1.3,1.3 q1,2.3 3.5,3.5 l1.3,-1.3 2.5,2 -1.6,1.8 q-4.5,-0.6 -7.8,-6.7Z" fill="var(--ink)"/></svg>123.456.7890</li>
    <li class="contact__item"><svg class="icon" viewBox="0 0 20 24"><rect x="5" y="3" width="10" height="20" rx="2" fill="none" stroke="var(--ink)" stroke-width="1.5"/><line x1="8" y1="20" x2="12" y2="20" stroke="var(--ink)"/></svg>123.456.7890</li>
    <li class="contact__item"><span class="social-square"></span>ourpage.com/</li>
  </ul>
  <div class="address">
    <svg class="icon" viewBox="0 0 10 14"><path d="M5,0 a4.5,4.5 0 0 1 4.5,4.5 c0,3 -4.5,9.5 -4.5,9.5 s-4.5,-6.5 -4.5,-9.5 A4.5,4.5 0 0 1 5,0Z" fill="var(--ink)"/><circle cx="5" cy="4.5" r="1.7" fill="var(--latte-light)"/></svg>
    <ul class="address__lines"><li>Address line 1</li><li>Address line 2</li><li>Address line 3</li></ul>
  </div>
  <div class="brand">Ladle</div>
</section>

</body>
</html>
```